Letterhead and Envelopes design using existing logo. Logo can be found at ridgemontcaldera.example

Use existing logo (attached) and incorporate in letterhead and envelope designs.

Current logo can be viewed at ridgemontcaldera.example the web site reflect various parent and sub companies. Please see attached as well.

Target Market(s)

Other oil and gas operators.

Industry/Entity Type

Oil And Gas

Font styles to use
Sans Serif

Colors

Designer to choose colors to be used in the design.

Requirements
Must have
• Current logo and address
Nice to have
• Modern, contemporary approach yet incorporate existing traditional design.
• After design is selected for Ridgemont Caldera Holdings I will use similar design for Royalties, Exploration, Energy and Farms with different color schemes.

```html
<!DOCTYPE html>
<html lang="en">
<head>
<meta charset="utf-8">
<title>Stationery – Option 02</title>
<link href="https://fonts.googleapis.com/css2?family=Arimo:wght@400;700&family=Roboto:wght@300&display=swap" rel="stylesheet">
<style>
  :root {
    --page: #ffffff;
    --label: #e4e4e6;
    --edge: #d6d6d8;
    --ink: #111111;
    --brand-green: #6a9a3a;
    --royalties-blue: #283a8a;
    --exploration-red: #c8264a;
    --ghost: #f0f0f1;
    --ghost-ring: #ebebec;
  }
  * { margin: 0; padding: 0; box-sizing: border-box; }
  html, body { width: 1200px; height: 1200px; overflow: hidden; background: var(--page); }
  body { position: relative; font-family: "Arimo", Arial, sans-serif; color: var(--ink); }

  .section-title, .piece-label {
    position: absolute;
    font-family: "Roboto", Arial, sans-serif;
    font-weight: 300;
    color: var(--label);
    line-height: 1;
  }
  .section-title { left: 62px; top: 94px; font-size: 58px; }
  .piece-label { font-size: 31px; }
  .piece-label--letterhead { left: 63px; top: 271px; }
  .piece-label--envelope { left: 838px; top: 442px; }

  /* Letterhead */
  .letterhead {
    position: absolute; left: 62px; top: 316px; width: 577px; height: 815px;
    border: 1px solid var(--edge); background: var(--page); overflow: hidden;
  }
  .brand-mark { position: absolute; display: flex; align-items: center; gap: 10px; }
  .brand-mark__dot { border-radius: 50%; background: var(--brand-green); flex: none; }
  .brand-mark__name { font-weight: 700; color: var(--ink); line-height: 1.15; }

  .letterhead .brand-mark { left: 48px; top: 49px; }
  .letterhead .brand-mark__dot { width: 64px; height: 64px; }
  .letterhead .brand-mark__name { font-size: 13px; width: 130px; }

  .ghost-seal {
    position: absolute; border-radius: 50%;
    border: 5px solid var(--ghost-ring);
    background: radial-gradient(circle closest-side, var(--ghost) 0 61%, transparent 62%);
  }
  .letterhead .ghost-seal { left: 118px; top: 444px; width: 340px; height: 340px; }

  .contact { position: absolute; }
  .contact__company { font-weight: 700; }
  .contact__line { display: flex; align-items: center; gap: 4px; }
  .contact__line svg { flex: none; }
  .letterhead .contact { left: 41px; top: 724px; }
  .letterhead .contact__company { font-size: 11.5px; margin-bottom: 2px; }
  .letterhead .contact__line { font-size: 9px; height: 12px; }

  .divisions { position: absolute; display: flex; align-items: flex-start; }
  .division { display: flex; flex-direction: column; align-items: center; gap: 3px; }
  .division__dot { border-radius: 50%; }
  .division__dot--royalties { background: var(--royalties-blue); }
  .division__dot--exploration { background: var(--exploration-red); }
  .division__name { font-weight: 700; text-align: center; line-height: 1.1; }
  .divisions__rule { background: var(--edge); align-self: stretch; }

  .letterhead .divisions { left: 417px; top: 723px; gap: 7px; }
  .letterhead .division { width: 52px; }
  .letterhead .division__dot { width: 44px; height: 44px; }
  .letterhead .division__name { font-size: 7px; }
  .letterhead .divisions__rule { width: 1px; }

  /* Envelope */
  .envelope-flap {
    position: absolute; left: 676px; top: 484px; width: 486px; height: 81px;
    border: 1px solid var(--edge); border-bottom: none;
    border-radius: 42px 42px 0 0; background: var(--page);
  }
  .envelope {
    position: absolute; left: 676px; top: 564px; width: 486px; height: 241px;
    border: 1px solid var(--edge); background: var(--page); overflow: hidden;
  }
  .envelope .brand-mark { left: 22px; top: 22px; }
  .envelope .brand-mark__dot { width: 56px; height: 56px; }
  .envelope .brand-mark__name { font-size: 11px; width: 110px; }
  .address-window {
    position: absolute; left: 13px; top: 102px; width: 175px; height: 62px;
    border: 1px solid var(--edge);
  }
  .envelope .ghost-seal { left: 326px; top: 66px; width: 156px; height: 156px; border-width: 3px; }
  .envelope .contact { left: 13px; top: 186px; }
  .envelope .contact__company { font-size: 9.6px; margin-bottom: 1px; }
  .envelope .contact__line { font-size: 7px; height: 9.6px; }
  .envelope .divisions { left: 362px; top: 17px; gap: 5px; }
  .envelope .division { width: 50px; }
  .envelope .division__dot { width: 44px; height: 44px; }
  .envelope .division__name { font-size: 6px; }
  .envelope .divisions__rule { width: 1px; }
</style>
</head>
<body>
  <h1 class="section-title">OPTION 02</h1>

  <h2 class="piece-label piece-label--letterhead">LETTERHEAD</h2>
  <section class="letterhead">
    <div class="brand-mark">
      <span class="brand-mark__dot"></span>
      <span class="brand-mark__name">Ridgemont Caldera Holdings</span>
    </div>

    <div class="ghost-seal" aria-hidden="true"></div>

    <div class="contact">
      <p class="contact__company">Ridgemont Caldera Holdings, LLC.</p>
      <p class="contact__line">PO Box 318 Larkfield, Montana 59410</p>
      <p class="contact__line">
        <svg width="12" height="8" viewBox="0 0 12 8"><rect width="12" height="8" fill="#111"/><path d="M0 0 L6 4.5 L12 0" stroke="#fff" stroke-width="1" fill="none"/></svg>
        : reception@ridgemontcaldera.example
      </p>
      <p class="contact__line">
        <svg width="11" height="11" viewBox="0 0 12 12"><circle cx="6" cy="6" r="5.3" fill="none" stroke="#111" stroke-width="1.2"/><ellipse cx="6" cy="6" rx="2.4" ry="5.3" fill="none" stroke="#111" stroke-width="1"/><path d="M0.7 6 H11.3 M1.6 3.4 H10.4 M1.6 8.6 H10.4" stroke="#111" stroke-width="0.9"/></svg>
        : www.ridgemontcaldera.example
      </p>
    </div>

    <div class="divisions">
      <div class="division">
        <span class="division__dot division__dot--royalties"></span>
        <span class="division__name">Ridgemont Royalties</span>
      </div>
      <span class="divisions__rule"></span>
      <div class="division">
        <span class="division__dot division__dot--exploration"></span>
        <span class="division__name">Ridgemont Exploration</span>
      </div>
    </div>
  </section>

  <h2 class="piece-label piece-label--envelope">ENVELOPE</h2>
  <div class="envelope-flap" aria-hidden="true"></div>
  <section class="envelope">
    <div class="brand-mark">
      <span class="brand-mark__dot"></span>
      <span class="brand-mark__name">Ridgemont Caldera Holdings</span>
    </div>

    <div class="ghost-seal" aria-hidden="true"></div>

    <div class="divisions">
      <div class="division">
        <span class="division__dot division__dot--royalties"></span>
        <span class="division__name">Ridgemont Royalties</span>
      </div>
      <span class="divisions__rule"></span>
      <div class="division">
        <span class="division__dot division__dot--exploration"></span>
        <span class="division__name">Ridgemont Exploration</span>
      </div>
    </div>

    <div class="address-window"></div>

    <div class="contact">
      <p class="contact__company">Ridgemont Caldera Holdings, LLC.</p>
      <p class="contact__line">PO Box 318 Larkfield, Montana 59410</p>
      <p class="contact__line">
        <svg width="10" height="7" viewBox="0 0 12 8"><rect width="12" height="8" fill="#111"/><path d="M0 0 L6 4.5 L12 0" stroke="#fff" stroke-width="1" fill="none"/></svg>
        : reception@ridgemontcaldera.example
      </p>
      <p class="contact__line">
        <svg width="9" height="9" viewBox="0 0 12 12"><circle cx="6" cy="6" r="5.3" fill="none" stroke="#111" stroke-width="1.2"/><ellipse cx="6" cy="6" rx="2.4" ry="5.3" fill="none" stroke="#111" stroke-width="1"/><path d="M0.7 6 H11.3 M1.6 3.4 H10.4 M1.6 8.6 H10.4" stroke="#111" stroke-width="0.9"/></svg>
        : www.ridgemontcaldera.example
      </p>
    </div>
  </section>
</body>
</html>
```